Broschüren-Design mit Werbeziel und Fokussierung auf Spendenaktion
Das Ergebnis ist toll. Die Designerin hat alles zu unseren Wünschen umgesetzt. Wir waren nicht die einfachsten Kunden, da wir doch einige Änderungen hatten. Aber nun sind wir zufrieden.
Zielgruppe
Wir sind Immobilienmakler und möchten neue Objekte generieren.
Zielgruppe sind Immobilienbesitzer ca. 40-70Jahre.
In dieser Broschüre machen wir gemeinsam mit 2 Handwerkern Werbung und machen gleichzeitig eine Spendenaktion.l
Aufgabenstellung
8 Seitige Broschüre Din A 4 Hoch.
Es soll schick und harmonisch aussehen.
Erste Seite sollen alle 3 Unternehmen aufgeführt werden. Entweder durch Logo oder Foto. Und wichtig, es soll auf die Spendenaktion aufmerksamgemacht werden. Z.B. gemeinsam gutes Tun. Oder 3 Gaildorfer Unternehmen spenden für Kinder.
Von Wendelin sind ein paar Quilvo Pics Bilder vorhanden. Es könne aber auch gerne neue Vorschläge kommen.
Seite 2-4: Tal-Immobilien Wendelin
Seite 2:
- Vorstellung Unternehmen. Standort Gaildorf und Backnang
-'Sie beauftragen uns mit dem Verkauf Ihrer Immobilie und wir Spenden nach dem Verkauf 500€ von unserer Provision. Die Spendenbescheinigung erhalten Sie als Nachweis.'
Referenzen von Kunden.
Seite 3: Wir suchen folgende Objekte.
- Seite 4:
Objektangebote.
Wichtig!!! Zu alle Objekten müssen die Angaben zum Energieausweis: Baujahr, Heizungsart, Verbrauchs- oder Bedarfsausweis, Energieeffizienzklasse und Energieklasse angegeben werden!!
- Seite 5: Home Staging.
- Seite 6: Fellbry Stuckatuer
- Seite 7: Ristel Holzbau
- Seite 8: Tal-Immobilien Wendelin.
Verbrieb: Tiny-House

```html
<!DOCTYPE html>
<html lang="de">
<head>
<meta charset="utf-8">
<title>Immobilien – Objektangebote</title>
<link href="https://fonts.googleapis.com/css2?family=Barlow:wght@400;500;600;700&display=swap" rel="stylesheet">
<style>
  :root {
    --gold: #b39c4a;
    --navy: #1e3657;
    --rule: #9aa7b8;
    --paper: #ffffff;
    --photo-sky: #b9cbe0;
  }
  * { box-sizing: border-box; margin: 0; padding: 0; }
  html, body { width: 960px; height: 1200px; overflow: hidden; background: var(--paper); }
  body { font-family: "Barlow", Arial, sans-serif; color: var(--navy); position: relative; }

  .page-title {
    position: absolute; left: 69px; top: 86px;
    font-size: 44px; font-weight: 500; letter-spacing: 1.5px;
    color: var(--gold);
  }
  .page-intro {
    position: absolute; left: 69px; top: 160px;
    font-size: 15px; font-weight: 700; line-height: 1.45; letter-spacing: 0.4px;
    color: var(--navy); text-transform: uppercase;
  }

  .listing {
    position: absolute; left: 60px; width: 831px; height: 122px;
    border-left: 1px solid var(--gold);
    border-bottom: 1px solid var(--gold);
  }
  .listing-photo {
    position: absolute; left: 9px; top: 0; width: 197px; height: 119px;
  }
  .listing-data {
    position: absolute; left: 248px; top: 0; width: 583px;
    display: grid; grid-template-columns: 292px 291px;
    font-size: 13px;
  }
  .listing-name {
    grid-column: 1 / 3; height: 24px; line-height: 24px; padding-left: 5px;
    background: var(--gold); color: #fff; font-weight: 600; font-size: 13.5px;
    white-space: nowrap; overflow: hidden;
  }
  .cell {
    height: 23px; line-height: 23px; padding-left: 5px;
    border-bottom: 1px solid var(--rule);
    white-space: nowrap;
  }
  .cell:nth-child(odd) { border-left: 1px solid var(--rule); border-right: 1px solid var(--rule); }
  sup { font-size: 8px; line-height: 0; }
</style>
</head>
<body>
  <h1 class="page-title">IMMOBILIEN</h1>
  <p class="page-intro">Immobilien zu einem fairen und<br>marktgerechten Preis</p>

  <section class="listing" style="top:241px">
    <div class="listing-photo" role="img" aria-label="Foto: Mehrfamilienhaus mit grauer Fassade" style="background:linear-gradient(180deg,#dfe3e8,#c2c7cd 60%,#8f969c)"></div>
    <div class="listing-data">
      <div class="listing-name">2 Zi-Wohnung mit Stellplatz in Bad-Cannstatt</div>
      <div class="cell">Baujahr: 1905</div><div class="cell">Energiekennwert: 111 KWh(m<sup>2</sup>*a)</div>
      <div class="cell">Wohnfläche: ca. 51 m<sup>2</sup></div><div class="cell">Energieeffizienzklasse: D</div>
      <div class="cell">Zustand: Saniert</div><div class="cell">Kaufpreis: 220.000 €</div>
      <div class="cell">Heizungsart: Zentralheizung / Gas</div><div class="cell"></div>
    </div>
  </section>

  <section class="listing" style="top:398px">
    <div class="listing-photo" role="img" aria-label="Foto: Dreifamilienhaus mit Holzbalkon" style="background:linear-gradient(180deg,var(--photo-sky),#e8dfcc 45%,#8a6a46 80%,#6d7a4e)"></div>
    <div class="listing-data">
      <div class="listing-name">Vermietetes 3 Familienhaus mit PV-Anlage in Gaildorf</div>
      <div class="cell">Baujahr: 1950</div><div class="cell">Energiekennwert: 0 KWh(m<sup>2</sup>*a)</div>
      <div class="cell">Wohnfläche: ca. 229m<sup>2</sup></div><div class="cell">Energieeffizienzklasse: A</div>
      <div class="cell">Zustand: Sehr gepflegt</div><div class="cell">Kaufpreis: 349.000 €</div>
      <div class="cell">Heizungsart: Zentralheizung / Gas</div><div class="cell"></div>
    </div>
  </section>

  <section class="listing" style="top:554px">
    <div class="listing-photo" role="img" aria-label="Foto: grün gestrichenes Dreifamilienhaus" style="background:linear-gradient(180deg,#2f63b8,#5d86c9 35%,#9aa54a 60%,#6f7d3a)"></div>
    <div class="listing-data">
      <div class="listing-name">3 Familienhaus komplett zum Sparhaus 100 saniert, Gerabronn</div>
      <div class="cell">Baujahr: 1968</div><div class="cell">Energiekennwert: 156 KWh(m<sup>2</sup>*a)</div>
      <div class="cell">Wohnfläche: ca. 324m<sup>2</sup></div><div class="cell">Energieeffizienzklasse: E</div>
      <div class="cell">Zustand: Saniert</div><div class="cell">Kaufpreis: 495.000 €</div>
      <div class="cell">Heizungsart: Zentralheizung / Pellet</div><div class="cell"></div>
    </div>
  </section>

  <section class="listing" style="top:711px">
    <div class="listing-photo" role="img" aria-label="Foto: helles Wohnzimmer mit Sofa" style="background:linear-gradient(180deg,#ece8e2,#d9d2c8 55%,#5b5450 75%,#b8aa98)"></div>
    <div class="listing-data">
      <div class="listing-name">Helle 5-Zimmer-Maisonettewohnung in Künzelsau</div>
      <div class="cell">Baujahr: 1994</div><div class="cell">Energiekennwert: 124 KWh(m<sup>2</sup>*a)</div>
      <div class="cell">Wohnfläche: ca. 109m<sup>2</sup></div><div class="cell">Energieeffizienzklasse: D</div>
      <div class="cell">Zustand: Sehr gepflegt</div><div class="cell">Kaufpreis: 239.000 €</div>
      <div class="cell">Heizungsart: Nahwärme</div><div class="cell"></div>
    </div>
  </section>

  <section class="listing" style="top:868px">
    <div class="listing-photo" role="img" aria-label="Foto: Einfamilienhaus mit Garten und Pergola" style="background:linear-gradient(180deg,var(--photo-sky),#e6e2dc 40%,#a4553a 60%,#7c9a4a)"></div>
    <div class="listing-data">
      <div class="listing-name">Schönes EFH mit Garten und Doppelgarage in top Lage, Gaildorf</div>
      <div class="cell">Baujahr: 0000</div><div class="cell">Energiekennwert: 000 KWh(m<sup>2</sup>*a)</div>
      <div class="cell">Wohnfläche: ca. 000m<sup>2</sup></div><div class="cell">Energieeffizienzklasse: D</div>
      <div class="cell">Zustand: Sehr gepflegt</div><div class="cell">Kaufpreis: 000.000 €</div>
      <div class="cell">Heizungsart: Nahwärme</div><div class="cell"></div>
    </div>
  </section>

  <section class="listing" style="top:1025px">
    <div class="listing-photo" role="img" aria-label="Foto: Wohn- und Geschäftshaus in der Innenstadt" style="background:linear-gradient(180deg,#c9d6e4,#e4e1dc 35%,#c8c2b8 75%,#7f8587)"></div>
    <div class="listing-data">
      <div class="listing-name">Wohn- und Geschäftshaus mitten in Gaildorf. Top Kapitalanlage</div>
      <div class="cell">Baujahr: 0000</div><div class="cell">Energiekennwert: 000 KWh(m<sup>2</sup>*a)</div>
      <div class="cell">Wohnfläche: ca. 000m<sup>2</sup></div><div class="cell">Energieeffizienzklasse: D</div>
      <div class="cell">Zustand: Sehr gepflegt</div><div class="cell">Kaufpreis: 000.000 €</div>
      <div class="cell">Heizungsart: Nahwärme</div><div class="cell"></div>
    </div>
  </section>
</body>
</html>
```